BASIC website restyle: graphic + coding

I need a restyle of our present website. Same contents, but better graphic.
It will be temporary until we'll have defined the strategy and so we'll have the definitive one.
I would need a fast job including coding.

I uploaded some picture that you're free to use.
I also extended of 1 day, no more extensions will be possible.

```html
<!DOCTYPE html>
<html lang="en">
<head>
<meta charset="utf-8">
<title>Verido – About us</title>
<link href="https://fonts.googleapis.com/css2?family=Arimo:wght@400;700&display=swap" rel="stylesheet">
<style>
  :root {
    --brand-green: #00873e;
    --dark-slate: #2e3a46;
    --text: #2b2b2b;
    --border: #d9d9d9;
    --white: #ffffff;
  }
  * { box-sizing: border-box; margin: 0; padding: 0; }
  html, body { width: 1200px; height: 956px; overflow: hidden; background: var(--white); }
  body { font-family: "Arimo", Arial, sans-serif; color: var(--text); position: relative; }

  .top-rule { position: absolute; left: 0; top: 0; width: 1200px; height: 3px; background: var(--dark-slate); }
  .bottom-rule { position: absolute; left: 0; bottom: 0; width: 1200px; height: 4px; background: var(--dark-slate); }

  .mail-tab {
    position: absolute; left: 868px; top: 3px; width: 162px; height: 28px;
    background: var(--dark-slate); border-radius: 0 0 4px 4px;
    display: flex; align-items: center; gap: 10px; padding-left: 14px;
    color: var(--white); font-size: 12px; text-decoration: underline; white-space: nowrap;
  }

  .brand { position: absolute; left: 170px; top: 28px; }
  .brand-name { font-size: 40px; font-weight: 700; color: var(--brand-green); line-height: 40px; letter-spacing: -1px; }

  .main-nav { position: absolute; top: 48px; left: 580px; width: 450px; height: 27px; }
  .main-nav a {
    position: absolute; top: 0; height: 27px; line-height: 27px;
    font-size: 11.5px; color: var(--text); text-decoration: none; white-space: nowrap;
  }
  .main-nav a.is-active { background: var(--brand-green); color: var(--white); width: 83px; text-align: center; }

  .hero {
    position: absolute; left: 0; top: 98px; width: 1200px; height: 395px;
    background:
      radial-gradient(ellipse at 20% 30%, rgba(214,222,150,0.75), transparent 55%),
      linear-gradient(160deg, transparent 55%, rgba(150,70,25,0.85) 80%),
      linear-gradient(90deg, #6f7d3a 0%, #4d5a22 35%, #3f4a1f 60%, #5b4a24 100%);
  }
  .hero-title {
    position: absolute; left: 387px; top: 176px; width: 427px; height: 44px;
    background: var(--brand-green); color: var(--white); white-space: nowrap;
    font-size: 22px; font-weight: 700; text-align: center; line-height: 44px;
  }
  .hero-arrow { position: absolute; top: 171px; }
  .hero-arrow.prev { left: 170px; }
  .hero-arrow.next { left: 976px; }
  .hero-shade { position: absolute; left: 0; top: 493px; width: 1200px; height: 18px;
    background: linear-gradient(#ececec, #ffffff); }

  .about-card {
    position: absolute; left: 170px; top: 524px; width: 860px; height: 300px;
    border: 1px solid var(--border); border-radius: 4px;
  }
  .about-copy { position: absolute; left: 20px; top: 17px; width: 420px; font-size: 11.3px; line-height: 14px; }
  .about-copy h1 { font-size: 22px; font-weight: 400; color: var(--brand-green); margin-bottom: 14px; line-height: 26px; }
  .about-copy p { margin-bottom: 13px; }
  .about-photo {
    position: absolute; left: 516px; top: 22px; width: 323px; height: 253px; border-radius: 4px;
    background: linear-gradient(180deg, #b6aa98 0%, #a09482 55%, #6f7488 80%, #3e4660 100%);
  }

  .footer-rule { position: absolute; left: 170px; top: 854px; width: 862px; height: 1px; background: #cfcfcf; }
  .social { position: absolute; top: 874px; left: 553px; display: flex; gap: 10px; }
  .social span { display: block; width: 25px; height: 25px; }
  .social .s-green { background: var(--brand-green); }
  .social .s-dark { background: var(--dark-slate); }
  .copyright { position: absolute; top: 909px; left: 0; width: 1200px; text-align: center; font-size: 12px; }
  .copyright strong { color: var(--brand-green); }
</style>
</head>
<body>
  <div class="top-rule"></div>

  <a class="mail-tab" href="#">
    <svg width="20" height="14" viewBox="0 0 20 14"><rect x="0.5" y="0.5" width="19" height="13" fill="none" stroke="#fff"/><path d="M1 1l9 7 9-7" fill="none" stroke="#fff"/></svg>
    info@verido.net
  </a>

  <header class="brand">
    <div class="brand-name">VERIDO</div>
  </header>

  <nav class="main-nav">
    <a style="left:19px" href="#">HOME</a>
    <a style="left:86px" href="#">FOREST</a>
    <a style="left:165px" href="#">AGRICULTURE</a>
    <a style="left:273px" href="#">TECHNOLOGY</a>
    <a class="is-active" style="left:367px" href="#">ABOUT US</a>
  </nav>

  <section class="hero" role="img" aria-label="Sunlit beech forest with autumn leaves on the ground">
    <div class="hero-title">INTERNET OF THINGS FOR FORESTS</div>
    <svg class="hero-arrow prev" width="54" height="54" viewBox="0 0 54 54"><circle cx="27" cy="27" r="27" fill="rgba(255,255,255,0.35)"/><path d="M31 16L20 27l11 11" fill="none" stroke="#fff" stroke-width="2.5"/></svg>
    <svg class="hero-arrow next" width="54" height="54" viewBox="0 0 54 54"><circle cx="27" cy="27" r="27" fill="rgba(255,255,255,0.35)"/><path d="M23 16l11 11-11 11" fill="none" stroke="#fff" stroke-width="2.5"/></svg>
  </section>
  <div class="hero-shade"></div>

  <main class="about-card">
    <div class="about-copy">
      <h1>ABOUT US</h1>
      <p>Verido is an high tech company specialised in Internet of Things.</p>
      <p>It has developed a unique Internet of Things framework for outdoor applications.</p>
      <p>Robust and reliable devices enable sophisticate analytics to support decision in Agriculture and Forests.</p>
      <p>Verido is based in Switzerland in Parco Tecno.</p>
      <p><strong>Verido SA</strong><br>CH6999 Valmonte (Parco Tecno)<br>Switzerland<br>info@verido.net</p>
      <p><strong>VAT number :</strong> CHE-000.123.456 IVA<br><strong>Register of commerce N.:</strong> CH-000.1.234.567-8</p>
    </div>
    <div class="about-photo" role="img" aria-label="Office building entrance with a tall sign and lavender shrubs in front"></div>
  </main>

  <div class="footer-rule"></div>
  <div class="social" aria-label="Social links">
    <span class="s-green"></span><span class="s-dark"></span><span class="s-dark"></span>
  </div>
  <p class="copyright">Copyright © <strong>VERIDO</strong> SA 2013. All rights reserved.</p>

  <div class="bottom-rule"></div>
</body>
</html>
```